Clay Sparrow- Hand made fashion accessories

Clay sparrow is a new business that will be selling hand made fashion accessories for women such as bags, baskets, knecklaces etc. The items are all hand made from Africa. I would like natural colors leaning more to the cardboard rustic look. I would like the card to look simple but elegant at the same time.

Industry/Entity Type

Business

Contact Information for Business Card

www.claysparrow-example.com.au
sales@claysparrow-example.com.au
Tel: 0452867310

Font styles to use
Decorative
Script

Requirements
Must have
• Earthy and rustic colours. Straw, cardboard etc. Fine black cursive print. One side of card only name
• second side website, email and tel.
Should not have
• No need to have any description of what business sells or does. No pictures of anything.

```html
<!DOCTYPE html>
<html lang="en">
<head>
<meta charset="utf-8">
<title>Clay Sparrow – Business Card</title>
<link rel="stylesheet" href="https://fonts.googleapis.com/css2?family=Dancing+Script:wght@400&family=Questrial&display=swap">
<style>
  :root {
    --backdrop: #8f8574;
    --kraft: #c9a878;
    --kraft-dark: #2a2019;
    --ink: #1c1510;
    --straw: #ecd9a8;
  }
  * { margin: 0; padding: 0; box-sizing: border-box; }
  html, body {
    width: 1105px;
    height: 1200px;
    overflow: hidden;
    background: var(--backdrop);
  }
  .canvas {
    position: relative;
    width: 1105px;
    height: 1200px;
  }
  .card {
    position: absolute;
    left: 184px;
    width: 745px;
    height: 427px;
  }
  .card--front {
    top: 119px;
    background: var(--kraft);
  }
  .card--back {
    top: 636px;
    background: var(--kraft-dark);
  }
  .brand-name {
    position: absolute;
    left: 0;
    top: 122px;
    width: 100%;
    text-align: center;
    font-family: "Questrial", sans-serif;
    font-weight: 400;
    font-size: 36px;
    line-height: 42px;
    letter-spacing: 2px;
    color: var(--ink);
  }
  .name-band {
    position: absolute;
    left: 0;
    top: 311px;
    width: 100%;
    height: 88px;
    background: var(--kraft-dark);
  }
  .holder-name {
    width: 720px;
    height: 88px;
    line-height: 88px;
    text-align: center;
    font-family: "Dancing Script", cursive;
    font-weight: 400;
    font-size: 48px;
    color: var(--straw);
    letter-spacing: 1px;
  }
  .contact {
    position: absolute;
    left: 0;
    top: 180px;
    width: 100%;
    text-align: center;
    font-family: "Questrial", sans-serif;
    font-size: 21px;
    line-height: 29px;
    color: var(--straw);
    list-style: none;
  }
</style>
</head>
<body>
<main class="canvas">
  <section class="card card--front" aria-label="Business card front">
    <p class="brand-name">Clay Sparrow</p>
    <div class="name-band">
      <p class="holder-name">Maya Thorne</p>
    </div>
  </section>

  <section class="card card--back" aria-label="Business card back">
    <ul class="contact">
      <li class="contact__phone">Tel: 0452867310</li>
      <li class="contact__email">sales@claysparrow-example.com.au</li>
      <li class="contact__web">www.claysparrow-example.com.au</li>
    </ul>
  </section>
</main>
</body>
</html>
```